Packaging design for Organic Beard Care brand - Stubble Meadow

This packaging design will be for our beard oil collection which include five different beard oil scents and our signature blend beard oil which is separate from the collection.
There will be two different variants of the box design needed:
Variant 1: White box with Logo and text (Ingredients, Directions, etc).
The words “Handcrafted Premium Beard Oil” will be printed in green foil color. Work this into the design.
Variant 2: Black box with gold foil logo and gold foil text (Ingredients, Directions, etc).
The words “Handcrafted Premium Beard Oil” will be printed in gold foil color. Work this into the design.
Both boxes should have a premium look and feel to it without too much noise.
(Think Kestra deodorant & shampoo brand or Plume teeth whitening brand)
Key callouts will be provided to add to the box designs.
I’ve attached icons, logos, images of the beard oil products and UPC codes that should be used on each box variant.
Please message me if there are more image assets or questions you have about creating the package design.
**Important** - You must create the design on the template file: 30ml-cardboard-box-template-stubble-meadow.ai. Any submissions without the design within this template will be passed up/rejected.
Men 21-50
Health & Beauty Cosmetics
- Miso, ASAP Condensed

```html
<!DOCTYPE html>
<html lang="en">
<head>
<meta charset="utf-8">
<title>Stubble Meadow – Beard Oil Box Panels</title>
<link href="https://fonts.googleapis.com/css2?family=Asap+Condensed:wght@400;500;600&family=Encode+Sans+Condensed:wght@500;600&display=swap" rel="stylesheet">
<style>
  :root {
    --stage: #2f2f30;
    --stage-dark: #232324;
    --panel: #ffffff;
    --panel-shade: #ececec;
    --ink: #3a3a3a;
    --ink-soft: #555555;
    --rule: #4a4a4a;
    --green-dark: #1f5a16;
    --green-mid: #3f8a23;
    --green-light: #8cc63f;
    --badge: #1c1c1c;
    --label: #ffffff;
  }
  * { box-sizing: border-box; margin: 0; padding: 0; }
  html, body { width: 1200px; height: 950px; overflow: hidden; }
  body {
    background: radial-gradient(ellipse at 50% 40%, var(--stage) 0%, var(--stage-dark) 100%);
    font-family: "Asap Condensed", "Arial Narrow", sans-serif;
    color: var(--ink);
    position: relative;
  }
  .panel {
    position: absolute;
    top: 88px;
    width: 237px;
    height: 690px;
    background: linear-gradient(180deg, var(--panel) 0%, var(--panel) 55%, var(--panel-shade) 100%);
    box-shadow: 18px 18px 30px rgba(0,0,0,0.45);
    text-align: center;
  }
  .panel--front-option { left: 89px; }
  .panel--side-one { left: 360px; }
  .panel--front { left: 644px; border-top: 2px solid var(--green-light); }
  .panel--side-two { left: 913px; }

  .abs { position: absolute; left: 0; right: 0; }
  .rule { position: absolute; left: 8px; right: 8px; height: 1px; background: var(--rule); }

  .seal {
    position: absolute; left: 50%; transform: translateX(-50%);
    display: flex; flex-direction: column; align-items: center;
  }
  .seal__dot { width: 40px; height: 40px; border-radius: 50%; background: var(--badge); }
  .seal__name { font-size: 12px; color: var(--ink); margin-top: 4px; white-space: nowrap; }

  .tagline {
    font-size: 13px; letter-spacing: 2.4px; text-transform: uppercase;
    color: var(--green-mid); font-weight: 500;
  }
  .headline {
    font-family: "Encode Sans Condensed", "Arial Narrow", sans-serif;
    font-weight: 600;
    background: linear-gradient(90deg, var(--green-dark) 0%, var(--green-mid) 45%, var(--green-light) 70%, var(--green-dark) 100%);
    -webkit-background-clip: text; background-clip: text; color: transparent;
    line-height: 1;
  }
  .scent { font-size: 11px; letter-spacing: 2px; text-transform: uppercase; }
  .scent--large { font-size: 16px; letter-spacing: 4px; }
  .callout { font-size: 11px; color: var(--ink-soft); }
  .netwt { font-size: 12px; }

  .foil-band {
    position: absolute; left: 0; right: 0; top: 600px; height: 24px;
    background: linear-gradient(90deg, var(--green-dark) 0%, var(--green-light) 25%, var(--green-mid) 45%, var(--green-dark) 55%, var(--green-light) 75%, var(--green-dark) 100%);
  }

  .section-title { font-size: 16px; font-weight: 600; letter-spacing: 1px; text-transform: uppercase; }
  .copy { font-size: 12px; line-height: 18.5px; padding: 0 18px; }
  .copy p + p { margin-top: 18px; }

  .panel-label {
    position: absolute; top: 830px; width: 237px; text-align: center;
    color: var(--label); font-size: 21px; font-weight: 600; letter-spacing: 0.5px;
    font-family: "Asap Condensed", "Arial Narrow", sans-serif;
  }
</style>
</head>
<body>

  <!-- Front option -->
  <section class="panel panel--front-option">
    <div class="seal" style="top:178px;">
      <div class="seal__dot"></div>
      <div class="seal__name">Stubble Meadow</div>
    </div>
    <div class="abs tagline" style="top:252px;">Handcrafted Premium</div>
    <div class="abs headline" style="top:270px; font-size:46px;">BEARD OIL</div>
    <div class="rule" style="top:344px;"></div>
    <div class="abs scent" style="top:348px;">Sweet Almond</div>
    <div class="rule" style="top:372px;"></div>
    <div class="abs callout" style="top:378px;">100% All-Natural &amp; Organic Ingredients</div>
    <div class="rule" style="top:402px;"></div>
    <div class="abs callout" style="top:408px;">None of that artificial stuff!</div>
    <div class="rule" style="top:432px;"></div>
    <div class="abs netwt" style="top:576px;">net wt. 30ml / 1 fl. oz.</div>
    <div class="foil-band"></div>
  </section>

  <!-- Side panel 1 -->
  <section class="panel panel--side-one">
    <div class="abs section-title" style="top:184px;">Directions</div>
    <div class="rule" style="top:211px;"></div>
    <div class="abs copy" style="top:222px;">
      <p>Squeeze 1–2 pulls of oil to the palm of your hand. For longer beards, use 3–4 pulls of oil.</p>
      <p>Rub hands together and massage into beard. Finish by styling as usual with a beard comb or pick to spread beard oil evenly throughout your beard.</p>
      <p>Use daily for best results.</p>
    </div>
    <div class="abs section-title" style="top:464px;">Ingredients</div>
    <div class="rule" style="top:491px;"></div>
    <div class="abs copy" style="top:502px;">
      <p>Castor Oil, Avocado Oil, Grapeseed Oil, Vitamin E, Sweet Almond Oil</p>
    </div>
  </section>

  <!-- Front -->
  <section class="panel panel--front">
    <div class="seal" style="top:52px;">
      <div class="seal__dot"></div>
      <div class="seal__name" style="font-size:13px;">Stubble Meadow</div>
    </div>
    <div class="abs tagline" style="top:130px; line-height:17px;">Handcrafted<br>Premium</div>
    <div class="rule" style="top:174px;"></div>
    <div class="abs headline" style="top:188px; font-size:48px;">BEARD</div>
    <div class="abs headline" style="top:236px; font-size:48px;">OIL</div>
    <div class="rule" style="top:297px;"></div>
    <div class="abs callout" style="top:306px; font-size:12px;">100% All-Natural &amp; Organic Ingredients</div>
    <div class="rule" style="top:332px;"></div>
    <div class="abs callout" style="top:338px;">None of that artificial stuff!</div>
    <div class="rule" style="top:362px;"></div>
    <div class="abs scent scent--large" style="top:546px;">Sweet Almond</div>
    <div class="rule" style="top:575px;"></div>
    <div class="abs netwt" style="top:588px;">net wt. 30ml / 1 fl. oz.</div>
  </section>

  <!-- Side panel 2 -->
  <section class="panel panel--side-two">
    <div class="seal" style="top:80px;">
      <div class="seal__dot"></div>
      <div class="seal__name">Stubble Meadow</div>
    </div>
    <div class="abs copy" style="top:176px;">
      <p>Stubble Meadow was created out of a necessity to provide beard oils that are made with natural and organic ingredients that would not be harmful to men who have skin sensitivities to heavy fragrances and artificial fillers.</p>
      <p>We have helped thousands of men keep their beards healthy and smelling good for over half a decade with amazing products and solid education on the many types of oils and ingredients that go into our beard oils and other beard care products.</p>
      <p>Our beard oils have been proven to prevent beard itch and beard dandruff while keeping your beard feeling soft and manageable everyday.</p>
    </div>
    <div class="rule" style="top:552px; left:10px; right:6px;"></div>
    <div class="abs copy" style="top:574px; text-transform:uppercase;">
      Quality ingredients.<br>Quality service. Everyday.
    </div>
  </section>

  <div class="panel-label" style="left:89px;">FRONT OPTION</div>
  <div class="panel-label" style="left:360px;">SIDE PANEL 1</div>
  <div class="panel-label" style="left:644px;">FRONT</div>
  <div class="panel-label" style="left:913px;">SIDE PANEL 2</div>

</body>
</html>
```